Short term Rentals Marketing agency needs Web design.

We Need a web design for our new company based in Calgary, AB. We are a International Luxury home sharing company (short term rental properties, Villas, Boutique Hotels, Bed & Breakfast, Realtors, Mortgage Brokers). We would like to see designs that look simple, modern and professional. Colors would be bold (red, black, white). The final design should communicate something welcoming, symbolize innovation, and growth. Our goal is to form partnerships with Real Estate, Property Management, Short term Rental Clients to make their lives easier and increase revenue. Vlto Harbor Co. offers a flexible and secure way to market our clients properties while maintaining client satisfaction and amazing customer service. We like how https://brinkleafpromo.ca/ is interactive (when you scroll down, text gets larger). Other similar websites for Short Term Rentals is https://www.quillnestgroup.com/, https://dwelvaroo.com/, https://www.kipmarsh.com/, https://www.tarnpenny.com/about-us/, https://vantrelstays.com. We have attached our Logo.

Target Market(s)

short term rental properties, Villas, Boutique Hotels, Bed & Breakfast, Realtors, Mortgage Brokers, property owners

Industry/Entity Type

Real Estate

Coding

Coded - Design and coding required

Number of Pages Required

5+ page

Font styles to use
Sans Serif

Requirements
Must have
• Home Page, About Us page, How it works, Services, Contact us.

We like how https://brinkleafpromo.ca/ is interactive (when you scroll down, text gets larger).

We have attached our Webcopy. We would like Call to Action Buttons where they're located in the copy and page.

Must have our Logo Colors.

Other similar websites for Short Term Rentals is https://www.quillnestgroup.com/, https://dwelvaroo.com/, https://www.kipmarsh.com/, https://www.tarnpenny.com/about-us/, https://vantrelstays.com.
Nice to have
• Catchy, Interactive Home page.

Should not have
• Should not be too cluttered

```html
<!DOCTYPE html>
<html lang="en">
<head>
<meta charset="utf-8">
<title>Vlto Harbor Co. — Home</title>
<link href="https://fonts.googleapis.com/css2?family=Poppins:wght@300;400;500;600;700&family=Oswald:wght@500&family=Montserrat:wght@900&display=swap" rel="stylesheet">
<style>
:root{
  --red:#e31e2f;
  --black:#0b0b0b;
  --white:#ffffff;
  --ink:#1a1a1a;
  --muted:#7a7a7a;
  --mist:#f1f2f7;
  --photo-sky:#6f8fb3;
  --photo-stone:#8a8176;
}
*{margin:0;padding:0;box-sizing:border-box}
html,body{width:1200px;height:4167px;overflow:hidden;background:var(--white)}
body{position:relative;font-family:'Poppins',sans-serif;color:var(--ink)}
.abs{position:absolute}
.brand{display:flex;align-items:center;gap:10px;font-family:'Poppins',sans-serif;font-weight:500;color:var(--ink);white-space:nowrap}
.brand-mark{width:28px;height:28px;background:var(--red);flex:0 0 auto}
.nav{top:28px;left:614px;display:flex;gap:26px;font-size:12px}
.nav a{color:var(--ink);text-decoration:none;position:relative}
.nav a.active{color:var(--red)}
.nav a.active::after{content:"";position:absolute;left:50%;top:20px;margin-left:-5px;border:5px solid transparent;border-bottom-color:var(--red)}
.search{left:1006px;top:21px;width:33px;height:33px;border-radius:50%;background:var(--red);display:flex;align-items:center;justify-content:center}
.hero-photo{left:0;top:281px;width:1200px;height:432px;background:linear-gradient(100deg,#2c3a4e 0%,#6d7f96 35%,#b9a98e 60%,#8b857c 100%)}
.hero-card{left:162px;top:105px;width:377px;height:360px;background:var(--red);color:var(--white);padding:78px 0 0 28px}
.hero-kicker{font-family:'Oswald',sans-serif;font-size:29px;line-height:1}
.hero-title{font-family:'Montserrat',sans-serif;font-weight:900;font-size:53px;line-height:1.08;margin-top:20px}
.btn{display:inline-block;position:relative;font-size:13px;text-transform:uppercase;color:var(--white);background:var(--red);padding:10px 22px;text-decoration:none;white-space:nowrap}
.btn.abs{position:absolute}
.btn::after{content:"";position:absolute;left:6px;top:6px;right:-6px;bottom:-6px;border:1px solid var(--red)}
.btn.dark{background:var(--black)}
.btn.dark::after{border-color:var(--black)}
.hero-card .btn{margin-top:26px}
.dots{left:1113px;top:437px;display:flex;flex-direction:column;gap:13px}
.dots span{width:11px;height:11px;border-radius:50%;background:rgba(255,255,255,.55)}
.dots span.on{background:var(--white);border:3px solid var(--red)}
.heading{font-size:40px;font-weight:600;text-align:center;width:1200px;left:0}
.heading em{font-style:normal;font-weight:300;color:var(--red)}
.feature{width:250px;text-align:center;top:865px}
.feature-icon{width:100px;height:100px;margin:0 auto;display:flex;align-items:center;justify-content:center}
.feature h3{font-size:17px;font-weight:500;line-height:1.35;margin-top:32px}
.feature p{font-size:11px;color:var(--muted);line-height:1.75;margin-top:18px}
.welcome-frame{left:348px;top:1321px;width:681px;height:517px;border:11px solid var(--red)}
.welcome-photo{left:171px;top:1523px;width:376px;height:375px;background:linear-gradient(180deg,var(--photo-sky) 0%,#9aa9b8 45%,var(--photo-stone) 65%,#e8eaee 82%)}
.welcome-text{left:640px;top:1396px;width:340px}
.welcome-text .kicker{font-size:15px;color:var(--red)}
.welcome-text h2{font-size:40px;font-weight:500;line-height:1.2;white-space:nowrap}
.welcome-text h2 em{font-style:normal;font-weight:300;color:var(--red)}
.welcome-text p{font-size:11px;color:var(--muted);line-height:1.9;margin-top:18px}
.welcome-text p+p{margin-top:10px}
.welcome-text .btn{margin-top:20px}
.services-bg{left:0;top:2081px;width:1200px;height:638px;background:var(--mist)}
.services-black{left:0;top:1981px;width:600px;height:300px;background:var(--black);color:var(--white);padding:65px 0 0 162px}
.services-black h2{font-size:40px;font-weight:600}
.services-black h2 em{font-style:normal;font-weight:300;color:var(--red)}
.services-black p{font-size:12.5px;line-height:1.7;width:310px;margin-top:12px}
.card{width:262px;height:194px;background:var(--white);border-radius:4px;padding:40px 28px 0 26px;box-shadow:0 2px 10px rgba(0,0,0,.04)}
.card.active{background:var(--red);color:var(--white)}
.card h4{font-size:15px;font-weight:400;line-height:1.4;margin-top:22px;width:125px}
.card .chev{position:absolute;right:36px;bottom:36px}
.how-band{left:0;top:2720px;width:1200px;height:336px;background:var(--red)}
.how-line{left:0;top:3053px;width:1200px;height:4px;background:var(--black)}
.how-head{top:2790px;width:1200px;left:0;text-align:center;color:var(--white)}
.how-head h2{font-size:40px;font-weight:600}
.how-head h2 span{font-weight:300}
.how-head p{font-size:12px;line-height:1.75;width:540px;margin:10px auto 0}
.step{width:260px;text-align:center;top:2964px}
.step-photo{width:178px;height:178px;border-radius:50%;margin:0 auto;border:6px solid var(--white);box-shadow:0 0 0 1px #ddd}
.step h3{font-size:17px;font-weight:500;margin-top:20px}
.step p{font-size:11px;color:var(--muted);line-height:1.8;margin-top:10px}
.contact-head{top:3468px;left:0;width:1200px;text-align:center}
.contact-head h2{font-size:40px;font-weight:600}
.contact-head h2 em{font-style:normal;font-weight:300;color:var(--red)}
.contact-head p{font-size:12.5px;line-height:1.8;width:420px;margin:10px auto 0;color:#333}
.house{left:299px;top:3622px;width:558px;height:200px;background:linear-gradient(180deg,#f3f1ee 0%,#b8ad9c 55%,#6e6458 100%)}
.footer{left:0;top:3821px;width:1200px;height:346px;background:var(--black);color:var(--white)}
.footer-brand{left:162px;top:3974px}
.footer-brand .brand{color:var(--white);font-size:23px;font-weight:400}
.footer-brand small{display:block;font-size:10px;margin-top:18px;color:var(--white)}
.col{top:3917px;color:var(--white)}
.col h5{font-size:15px;font-weight:400;margin-bottom:18px}
.col ul{list-style:none;font-size:10.5px;line-height:2.5;color:#cfcfcf}
.col li::before{content:"";display:inline-block;width:4px;height:4px;border-radius:50%;background:var(--red);margin-right:14px;vertical-align:middle}
.contact-row{display:flex;gap:18px;font-size:10.5px;line-height:1.7;color:#cfcfcf;margin-bottom:22px;width:200px}
.contact-row svg{flex:0 0 auto}
.foot-bar{left:527px;top:4162px;width:144px;height:5px;background:var(--red)}
</style>
</head>
<body>

<header>
  <div class="abs brand" style="left:162px;top:22px;font-size:22px">
    <span class="brand-mark"></span>Vlto Harbor Co.
  </div>
  <nav class="abs nav">
    <a class="active" href="#">Home</a><a href="#">About Us</a><a href="#">How It Works</a><a href="#">Services</a><a href="#">Contact Us</a>
  </nav>
  <div class="abs search">
    <svg width="13" height="13" viewBox="0 0 13 13"><circle cx="5.5" cy="5.5" r="4" fill="none" stroke="#fff" stroke-width="1.8"/><line x1="8.5" y1="8.5" x2="12" y2="12" stroke="#fff" stroke-width="1.8"/></svg>
  </div>
</header>

<section>
  <div class="abs hero-photo" role="img" aria-label="Modern luxury villa with timber slat facade beside a city skyline at dusk"></div>
  <div class="abs hero-card">
    <div class="hero-kicker">Partner with Us &amp; Let's Start</div>
    <div class="hero-title">GROWING<br>TOGETHER</div>
    <a class="btn dark" href="#">Work with us</a>
  </div>
  <div class="abs dots"><span></span><span></span><span></span><span class="on"></span><span></span></div>
</section>

<section>
  <h2 class="abs heading" style="top:780px">Why <em>Choose Us</em></h2>

  <div class="abs feature" style="left:176px">
    <div class="feature-icon">
      <svg width="60" height="60" viewBox="0 0 60 60"><path d="M30 6 54 30 30 54 6 30Z" fill="#fff" stroke="#eee" stroke-width="1"/><circle cx="30" cy="36" r="9" fill="none" stroke="#111" stroke-width="1.8"/><circle cx="30" cy="36" r="5" fill="var(--red)"/><path d="M30 26V12M25 17l5-5 5 5" fill="none" stroke="#111" stroke-width="1.8"/></svg>
    </div>
    <h3>Increase Your<br>Revenue</h3>
    <p>Having Vlto Harbor Co. manage and market your rental property lets you benefit from increased revenues without having to put in the hours of work yourself. Vlto Harbor Co. will manage your property listings, advertise your listings.</p>
  </div>

  <div class="abs feature" style="left:478px">
    <div class="feature-icon">
      <svg width="60" height="60" viewBox="0 0 60 60"><path d="M30 6 54 30 30 54 6 30Z" fill="#fff" stroke="#eee" stroke-width="1"/><circle cx="30" cy="24" r="7" fill="none" stroke="#111" stroke-width="1.8"/><path d="M18 46c0-8 5-12 12-12s12 4 12 12Z" fill="none" stroke="#111" stroke-width="1.8"/><path d="M28 35h4l-2 8Z" fill="var(--red)"/></svg>
    </div>
    <h3>Receive Constant<br>Support</h3>
    <p>Our dedicated team is there to take care of your property so that you don't have to. Our affordable and professional services include being there to support your guests, constant technical communication, &amp; on-site operations management.</p>
  </div>

  <div class="abs feature" style="left:781px">
    <div class="feature-icon">
      <svg width="60" height="60" viewBox="0 0 60 60"><path d="M30 6 54 30 30 54 6 30Z" fill="#fff" stroke="#eee" stroke-width="1"/><path d="M20 28 30 18 40 28V38H20Z" fill="var(--red)"/><path d="M14 30c0 10 6 16 16 16s16-6 16-16" fill="none" stroke="#111" stroke-width="1.8"/></svg>
    </div>
    <h3>Manage Your Risks<br>and Insurance</h3>
    <p>Vlto Harbor Co. will help you protect your property income by giving you the security and insurance you need when it comes to pricing and managing your security deposits. Please note that terms and conditions apply.</p>
  </div>

  <a class="abs btn" href="#" style="left:530px;top:1193px">Work with us</a>
</section>

<section>
  <div class="abs welcome-frame"></div>
  <div class="abs welcome-photo" role="img" aria-label="Large stone and timber luxury home in winter"></div>
  <div class="abs welcome-text">
    <div class="kicker">welcome to</div>
    <h2>Vlto <em>Harbor Co.</em></h2>
    <p>Vlto Harbor Co. is here to manage and market your short-term rental properties so you don't have to. Enjoy peace of mind in knowing your short-term rental properties, vacation homes, villas, hotels, &amp; B&amp;Bs are safe, secure, and profitable – no matter where you are in the world. We will help you market, manage, &amp; capitalize on everything, from your newest bookings to house cleaning &amp; upkeep.</p>
    <p>Vlto Harbor Co. saves you time, money, &amp; effort, so that you can focus on the things that matter most to you. Let us help you increase your rental revenue in a simple…</p>
    <a class="btn" href="#">Learn more</a>
  </div>
</section>

<section>
  <div class="abs services-bg"></div>
  <div class="abs services-black">
    <h2>Our <em>Services</em></h2>
    <p>Our friendly and welcoming team of experts is dedicated to meeting every one of your needs &amp; exceeding your expectations.</p>
  </div>

  <div class="abs card" style="left:179px;top:2225px">
    <svg width="56" height="50" viewBox="0 0 56 50"><path d="M8 14 26 6 44 14V36L26 44 8 36Z M8 14 26 22 44 14 M26 22V44" fill="none" stroke="#111" stroke-width="1.6"/><path d="M40 38l4 4 8-8" fill="none" stroke="#111" stroke-width="1.6"/></svg>
    <h4>Import and Export Auto Ratings</h4>
    <svg class="chev" width="14" height="24" viewBox="0 0 14 24"><path d="M2 2l10 10-10 10" fill="none" stroke="currentColor" stroke-width="3"/></svg>
  </div>
  <div class="abs card active" style="left:469px;top:2225px">
    <svg width="60" height="50" viewBox="0 0 60 50"><path d="M4 46H56M10 46V24L30 8 50 24V46M22 46V32H38V46" fill="none" stroke="#fff" stroke-width="1.6"/></svg>
    <h4>Direct<br>Bookings</h4>
    <svg class="chev" width="14" height="24" viewBox="0 0 14 24"><path d="M2 2l10 10-10 10" fill="none" stroke="currentColor" stroke-width="3"/></svg>
  </div>
  <div class="abs card" style="left:757px;top:2225px">
    <svg width="56" height="50" viewBox="0 0 56 50"><rect x="14" y="4" width="28" height="42" rx="3" fill="none" stroke="#111" stroke-width="1.6"/><circle cx="28" cy="16" r="6" fill="none" stroke="var(--red)" stroke-width="1.6"/><path d="M20 38V30M26 38V26M32 38V32M38 38V28" stroke="#111" stroke-width="2"/></svg>
    <h4>Powerful<br>Reporting</h4>
    <svg class="chev" width="14" height="24" viewBox="0 0 14 24"><path d="M2 2l10 10-10 10" fill="none" stroke="currentColor" stroke-width="3"/></svg>
  </div>
  <div class="abs card" style="left:179px;top:2450px">
    <svg width="60" height="50" viewBox="0 0 60 50"><path d="M6 34c10-4 20-4 30 0-4 8-24 8-30 0Z" fill="var(--red)"/><path d="M36 30 50 10" stroke="#111" stroke-width="1.8"/><path d="M46 6l4 4M54 20l3 3" stroke="#111" stroke-width="1.6"/></svg>
    <h4>Cleaning and Organization</h4>
    <svg class="chev" width="14" height="24" viewBox="0 0 14 24"><path d="M2 2l10 10-10 10" fill="none" stroke="currentColor" stroke-width="3"/></svg>
  </div>
  <div class="abs card" style="left:469px;top:2450px">
    <svg width="60" height="50" viewBox="0 0 60 50"><rect x="8" y="6" width="44" height="30" rx="2" fill="none" stroke="#111" stroke-width="1.6"/><circle cx="30" cy="18" r="5" fill="none" stroke="var(--red)" stroke-width="1.6"/><path d="M20 32c2-6 18-6 20 0M22 44h16M30 36v8" fill="none" stroke="#111" stroke-width="1.6"/></svg>
    <h4>Customer Communication</h4>
    <svg class="chev" width="14" height="24" viewBox="0 0 14 24"><path d="M2 2l10 10-10 10" fill="none" stroke="currentColor" stroke-width="3"/></svg>
  </div>
  <div class="abs card" style="left:757px;top:2450px">
    <svg width="56" height="50" viewBox="0 0 56 50"><rect x="6" y="8" width="44" height="36" rx="2" fill="none" stroke="#111" stroke-width="1.6"/><path d="M6 18H50M16 4v8M40 4v8" stroke="#111" stroke-width="1.6"/><rect x="14" y="24" width="10" height="7" fill="var(--red)"/><rect x="30" y="32" width="10" height="7" fill="var(--red)"/></svg>
    <h4>Calendar Adjustments</h4>
    <svg class="chev" width="14" height="24" viewBox="0 0 14 24"><path d="M2 2l10 10-10 10" fill="none" stroke="currentColor" stroke-width="3"/></svg>
  </div>
</section>

<section>
  <div class="abs how-band"></div>
  <div class="abs how-line"></div>
  <div class="abs how-head">
    <h2>How <span>It Work</span></h2>
    <p>We try to keep our application, management, and marketing process as quick and simple as possible. To sign up to Vlto Harbor Co., you can follow these three steps:</p>
  </div>

  <div class="abs step" style="left:177px">
    <div class="step-photo" role="img" aria-label="Couple booking a consultation on a laptop" style="background:linear-gradient(160deg,#e9e4de,#b8a797)"></div>
    <h3>Book A Consultation</h3>
    <p>Give us a call to set up your own consultation session where we will discuss your needs, goals, and concerns regarding the management and marketing of your short-term rental properties.</p>
  </div>
  <div class="abs step" style="left:470px">
    <div class="step-photo" role="img" aria-label="Luxury home with pool at twilight" style="background:linear-gradient(180deg,#2f6fb8 0%,#8fb3d8 50%,#6c6a60 75%,#4aa3c8 100%)"></div>
    <h3>Optimize Your Property</h3>
    <p>Once you've decided what you would like from your rental property, we will help you make it a reality. This involves optimizing your pricing, listings, operations, bookings, and much more.</p>
  </div>
  <div class="abs step" style="left:777px">
    <div class="step-photo" role="img" aria-label="Host welcoming renters in an office" style="background:linear-gradient(160deg,#d7d3cc,#5a6b7c)"></div>
    <h3>Start Hosting Renters</h3>
    <p>You can start hosting renters in no time thanks to our quick turnaround times and professional services. We will help you maintain your properties for as long as you need us.</p>
  </div>

  <a class="abs btn" href="#" style="left:527px;top:3331px">Work with us</a>
</section>

<section>
  <div class="abs contact-head">
    <h2>Contact <em>Us Today</em></h2>
    <p>One of our Expert Team Members will be in touch to start discussing your needs and potential questions. We look forward to working with you!</p>
  </div>
  <div class="abs house" role="img" aria-label="Stone family house with dark shingled roof and garage doors"></div>
</section>

<footer>
  <div class="abs footer"></div>
  <a class="abs btn" href="#" style="left:493px;top:3810px;z-index:2">Let's get started today</a>

  <div class="abs footer-brand">
    <div class="brand"><span class="brand-mark" style="width:32px;height:32px"></span>Vlto Harbor Co.</div>
    <small>©Vlto Harbor Co. - 2020 All rights reserved.</small>
  </div>

  <div class="abs col" style="left:433px">
    <h5>Sitemap</h5>
    <ul><li>Home</li><li>About Us</li><li>How it works</li><li>Services</li><li>Contact us</li></ul>
  </div>
  <div class="abs col" style="left:614px">
    <h5>Services</h5>
    <ul><li>Import &amp; Export Auto Ratings</li><li>Direct Bookings</li><li>Powerful Reporting</li><li>Cleaning and Organization</li><li>Customer Communication</li><li>Calendar Adjustments</li></ul>
  </div>
  <div class="abs col" style="left:851px">
    <h5>Contact Us</h5>
    <div class="contact-row">
      <svg width="14" height="18" viewBox="0 0 14 18"><path d="M7 17S1 10 1 6.5a6 6 0 0 1 12 0C13 10 7 17 7 17Z" fill="var(--red)"/><circle cx="7" cy="6.5" r="2.2" fill="#000"/></svg>
      <div><span style="color:#fff">Vlto Harbor Co.</span><br>101 - Lorem ipsum simple the text print type industry.</div>
    </div>
    <div class="contact-row">
      <svg width="16" height="16" viewBox="0 0 16 16"><path d="M3 1l3 3-2 2c1 2.5 3.5 5 6 6l2-2 3 3-2 2C7 15 1 9 1 3Z" fill="var(--red)"/></svg>
      <div>403 555 0186</div>
    </div>
    <div class="contact-row">
      <svg width="16" height="12" viewBox="0 0 16 12"><rect width="16" height="12" rx="1" fill="var(--red)"/><path d="M1 1l7 6 7-6" fill="none" stroke="#000" stroke-width="1.3"/></svg>
      <div>info@vltoharbor.co</div>
    </div>
  </div>
  <div class="abs foot-bar"></div>
</footer>

</body>
</html>
```